Business card for our start up Automotive Shop

Clean business card design for our new automotive shop Brightline Motor Works. This card will be the template for all of our staff member including technicians and service advisors.

Brightline Motor Works is an automotive service shop catering to US domestic and asian import vehicles. We are a service and maintenance full service facility. Our aim is to provide the best quality workmanship and the best customer service experience in our industry.

Our target market are young professionals to people with families. We are not targeting a younger audience or the car modification scene. The card should be appealing to women of the 30+ age demographic.

We are a shop of younger professionals instead of an older crowd. The card design should reflect as such.

Target Market(s)

30+ Female demographic and 30+ male.

Industry/Entity Type

Automotive

Contact Information for Business Card

Must be clean and appealing to clients. Large enough and easy to read print.

Font styles to use
Sans Serif

Colors
f78f20
ffffff
b2b2b2
dddddd

Requirements
Must have
• Address, website and phone number
• 42-15 58th Ave
• Cedar Hollow NY 11462
• (718) 402-3917
• brightlinemotorworks.com
• There must be an area to add a Name and e-mail address for personalization purposes.
Nice to have
• Back of the card should have website.
• I would also like to incorporate yelp, google+, Facebook, and instagram widgets. Will add the exact pages but everything can be @ or / brightlinemotorworks
• That can be added on the back of the card.

```html
<!DOCTYPE html>
<html lang="en">
<head>
<meta charset="utf-8">
<title>Brightline Motor Works – Business Card</title>
<link rel="stylesheet" href="https://fonts.googleapis.com/css2?family=Exo+2:wght@400;500;700;800&display=swap">
<style>
  :root {
    --orange: #f78f20;
    --white: #ffffff;
    --grey: #b2b2b2;
    --light-grey: #dddddd;
    --card: #1b1b1b;
    --stage: #2b2b2b;
  }
  * { box-sizing: border-box; margin: 0; padding: 0; }
  html, body {
    width: 1200px;
    height: 900px;
    overflow: hidden;
    background: var(--stage);
    font-family: "Exo 2", sans-serif;
  }
  .canvas {
    width: 1200px;
    height: 900px;
    display: flex;
    flex-direction: column;
    align-items: center;
    justify-content: center;
    gap: 40px;
  }
  .card {
    position: relative;
    width: 640px;
    height: 366px;
    background: var(--card);
    overflow: hidden;
  }

  /* Back side */
  .card-back .brand {
    position: absolute;
    left: 0; right: 0; top: 110px;
    display: flex;
    align-items: center;
    justify-content: center;
    gap: 18px;
  }
  .brand-dot {
    width: 62px;
    height: 62px;
    border-radius: 50%;
    background: var(--orange);
    flex: none;
  }
  .brand-name {
    color: var(--orange);
    font-weight: 700;
    text-transform: uppercase;
    line-height: 1.05;
  }
  .card-back .brand-name { font-size: 34px; letter-spacing: 1px; }
  .brand-name .line-2 { display: block; letter-spacing: 7px; font-size: 0.62em; }
  .card-back .site {
    position: absolute;
    left: 0; right: 0; top: 252px;
    text-align: center;
    color: var(--light-grey);
    font-size: 13px;
    letter-spacing: 4px;
  }

  /* Front side */
  .tab {
    position: absolute;
    left: 0; top: 28px;
    width: 14px; height: 48px;
    background: var(--orange);
    border-radius: 0 24px 24px 0;
  }
  .person { position: absolute; left: 44px; top: 30px; }
  .person-name {
    color: var(--white);
    font-weight: 800;
    font-size: 27px;
    letter-spacing: 1.5px;
    text-transform: uppercase;
  }
  .person-role {
    color: var(--orange);
    font-size: 17px;
    font-weight: 500;
    letter-spacing: 1px;
    margin-top: -2px;
  }
  .card-front .brand-name {
    position: absolute;
    right: 40px; top: 88px;
    font-size: 31px;
    letter-spacing: 1px;
    text-align: left;
  }
  .contact {
    position: absolute;
    left: 44px; top: 188px;
    color: var(--white);
    font-size: 16px;
    letter-spacing: 1px;
    line-height: 1.5;
  }
  .contact-row { display: flex; align-items: center; gap: 10px; }
  .contact-row svg { width: 14px; height: 14px; flex: none; }
  .address { margin-top: 12px; }
  .social {
    position: absolute;
    right: 40px; bottom: 50px;
    display: flex;
    align-items: center;
    gap: 10px;
    color: var(--white);
    font-size: 16px;
    letter-spacing: 1px;
  }
  .social-dot {
    width: 12px; height: 12px;
    border-radius: 50%;
    background: var(--orange);
  }
  .band {
    position: absolute;
    left: 0; right: 0; bottom: 0;
    height: 22px;
    background: var(--orange);
  }
</style>
</head>
<body>
<main class="canvas">

  <section class="card card-back" aria-label="Card back">
    <div class="brand">
      <span class="brand-dot"></span>
      <p class="brand-name">Brightline<span class="line-2">Motor Works</span></p>
    </div>
    <p class="site">brightlinemotorworks.co</p>
  </section>

  <section class="card card-front" aria-label="Card front">
    <span class="tab"></span>
    <div class="person">
      <p class="person-name">Dana Whitfield</p>
      <p class="person-role">Founder</p>
    </div>

    <p class="brand-name">Brightline<span class="line-2">Motor Works</span></p>

    <div class="contact">
      <p class="contact-row">
        <svg viewBox="0 0 14 14" aria-hidden="true"><rect x="3.5" y="1" width="7" height="12" rx="1.2" fill="none" stroke="#f78f20" stroke-width="1.4"/><line x1="6" y1="11" x2="8" y2="11" stroke="#f78f20" stroke-width="1.2"/></svg>
        (718) 402-3917
      </p>
      <p class="contact-row">
        <svg viewBox="0 0 14 14" aria-hidden="true"><circle cx="6" cy="6" r="4" fill="none" stroke="#f78f20" stroke-width="1.8"/><line x1="9" y1="9" x2="12.5" y2="12.5" stroke="#f78f20" stroke-width="2" stroke-linecap="round"/></svg>
        brightlinemotorworks.com
      </p>
      <p class="address">42-15 58th Ave<br>Cedar Hollow NY 11462</p>
    </div>

    <div class="social">
      <span class="social-dot"></span>
      <span>brightlinemotorworks</span>
    </div>

    <span class="band"></span>
  </section>

</main>
</body>
</html>
```